Australian Software Consultancy needs new Business Card Design

Design Business Card based on existing design artefacts (attached). We are open to all designs. As its a 2 sided design and we thought it might be quite striking to have one side with a black background and te other side with a white background.

Target Market(s)

Financial Services mainly.

Industry/Entity Type

Business

Contact Information for Business Card

Requirements
Must have
• Funky design using our existing assets

```html
<!DOCTYPE html>
<html lang="en">
<head>
<meta charset="utf-8">
<title>North Peak Business Card</title>
<link rel="stylesheet" href="https://fonts.googleapis.com/css2?family=Montserrat:wght@600;700&family=Open+Sans:wght@400;600&display=swap">
<style>
  :root {
    --backdrop: #6b6b6b;
    --card-light: #f2f2f2;
    --card-dark: #000000;
    --brand-red: #ec1c24;
    --ink: #111111;
    --ink-soft: #3a3a3a;
  }
  * { margin: 0; padding: 0; box-sizing: border-box; }
  html, body { width: 1200px; height: 900px; overflow: hidden; }
  body {
    background: var(--backdrop);
    position: relative;
    font-family: "Open Sans", Arial, sans-serif;
  }
  .card {
    position: absolute;
    top: 170px;
    width: 347px;
    height: 560px;
    box-shadow: 0 2px 6px rgba(0,0,0,0.25);
  }
  .card--front { left: 259px; background: var(--card-light); }
  .card--back { left: 631px; background: var(--card-dark); }

  .brand-ring {
    position: absolute;
    border-radius: 50%;
    border: 7px solid var(--brand-red);
  }
  .card--front .brand-ring { left: 113px; top: 60px; width: 120px; height: 120px; }
  .card--back .brand-ring { left: 64px; top: 171px; width: 219px; height: 219px; border-width: 11px; }

  .brand-name {
    position: absolute;
    left: 0; right: 0;
    text-align: center;
    font-family: "Montserrat", Arial, sans-serif;
    font-weight: 700;
    text-transform: uppercase;
  }
  .card--front .brand-name { top: 200px; font-size: 40px; color: var(--ink); letter-spacing: 0.5px; }
  .card--back .brand-name { top: 265px; font-size: 26px; color: var(--brand-red); }

  .person {
    position: absolute;
    left: 0; right: 0;
    top: 403px;
    text-align: center;
  }
  .person__name {
    font-family: "Montserrat", Arial, sans-serif;
    font-weight: 600;
    font-size: 22px;
    color: var(--ink);
    line-height: 30px;
  }
  .person__name .accent { color: var(--brand-red); }
  .person__role { font-size: 14px; color: var(--ink-soft); line-height: 20px; }

  .contact {
    position: absolute;
    left: 0; right: 0;
    top: 476px;
    text-align: center;
    font-size: 14px;
    line-height: 21px;
    color: var(--ink-soft);
    list-style: none;
  }
  .contact__label { color: var(--brand-red); font-weight: 600; }

  .website {
    position: absolute;
    left: 0; right: 0;
    top: 489px;
    text-align: center;
    font-family: "Montserrat", Arial, sans-serif;
    font-weight: 700;
    font-size: 14px;
    letter-spacing: 0.3px;
    color: var(--brand-red);
  }
</style>
</head>
<body>
  <section class="card card--front">
    <div class="brand-ring"></div>
    <div class="brand-name">North Peak</div>
    <div class="person">
      <p class="person__name">Alex <span class="accent">Carter</span></p>
      <p class="person__role">Managing Director</p>
    </div>
    <ul class="contact">
      <li><span class="contact__label">P:</span> 555-014-2870</li>
      <li><span class="contact__label">E:</span> hello@northpeak.com</li>
    </ul>
  </section>

  <section class="card card--back">
    <div class="brand-ring"></div>
    <div class="brand-name">North Peak</div>
    <p class="website">www.northpeak.com</p>
  </section>
</body>
</html>
```